Naturopath specialising in Children's Health

I have just started working in a new clinic where I will be predominantly treating children so I would like to rebrand with a business card that reflects this.

I would like a clever design which is subtly playful and will attract children and parents alike, while maintaining a professional look. It must also reflect that I utilize natural medicine - including herbal medicine and nutrition as part of my treatment. Employing the use of a plant or herb would be ideal. I had envisioned the image of a dandelion blowing in the wind (or being blown by a child) as a great combination of the playful yet natural medicine I am trying to ecompass in the card.

I would like to use yellow, orange, blue or green as the dominant colour for the card.

The front of the card should contain the logo and the words 'Maribel Stroud - Naturopath.'

The back of the card should contain the following details:
Maribel Stroud BHSc Nat, Dip RM
Naturopath, Herbalist, Nutritionist, Iridologist, Remedial Massage Therapist, Reiki Practitioner
0413 927 186
Willowfern Haven - (02) 9731 4068
maribel.stroud@kestrelmail.example
NHPA 81347

Industry/Entity Type

Clinic

```html
<!DOCTYPE html>
<html lang="en">
<head>
<meta charset="utf-8">
<title>Maribel Stroud – Naturopath Business Card</title>
<link rel="stylesheet" href="https://fonts.googleapis.com/css2?family=Jost:wght@400;500&family=Gelasio:wght@400;700&display=swap">
<style>
  :root {
    --page-bg: #ecebe7;
    --forest: #036b36;
    --forest-light: #2f8a52;
    --lime: #8fd52a;
    --white: #ffffff;
    --ink: #111111;
    --ink-soft: #222222;
    --rule: #555555;
  }
  html, body {
    margin: 0;
    width: 1200px;
    height: 1000px;
    overflow: hidden;
    background: var(--page-bg);
  }
  .canvas {
    position: relative;
    width: 1200px;
    height: 1000px;
  }
  .card {
    position: absolute;
    left: 282px;
    width: 676px;
    height: 390px;
    border-radius: 18px;
    overflow: hidden;
    box-shadow: 0 4px 10px rgba(0,0,0,0.25);
  }
  /* Front */
  .card-front {
    top: 70px;
    background: var(--forest);
  }
  .dandelion-cluster {
    position: absolute;
    left: 8px;
    top: 6px;
    width: 186px;
    height: 384px;
    border-radius: 90px 90px 0 0;
    background: linear-gradient(180deg, rgba(255,255,255,0.62) 0%, rgba(255,255,255,0.42) 55%, rgba(255,255,255,0.78) 100%);
  }
  .drifting-seeds {
    position: absolute;
    left: 236px;
    top: 16px;
    width: 392px;
    height: 150px;
    border-radius: 75px;
    background: linear-gradient(90deg, rgba(255,255,255,0.22) 0%, rgba(255,255,255,0.42) 100%);
  }
  .name-band {
    position: absolute;
    left: 283px;
    top: 253px;
    width: 393px;
    height: 82px;
    background: var(--lime);
    color: var(--white);
    text-align: center;
    font-family: "Jost", sans-serif;
  }
  .name-band .name {
    margin: 4px 0 0;
    font-size: 37px;
    font-weight: 500;
    font-variant: small-caps;
    letter-spacing: 1px;
    line-height: 44px;
  }
  .name-band .role {
    margin: 0;
    font-size: 22px;
    font-weight: 400;
    line-height: 26px;
    letter-spacing: 0.5px;
  }
  /* Back */
  .card-back {
    top: 498px;
    height: 388px;
    background: var(--white);
    border: 1px solid var(--forest-light);
    box-sizing: border-box;
    font-family: "Gelasio", serif;
    color: var(--ink);
  }
  .back-name {
    position: absolute;
    left: 25px;
    top: 28px;
    margin: 0;
    font-size: 27px;
    font-weight: 700;
  }
  .credentials {
    position: absolute;
    left: 25px;
    top: 62px;
    margin: 0;
    font-size: 19px;
  }
  .modalities {
    position: absolute;
    left: 25px;
    top: 96px;
    margin: 0;
    font-size: 15.5px;
    line-height: 23px;
    color: var(--ink-soft);
  }
  .divider {
    position: absolute;
    left: 8px;
    right: 8px;
    top: 271px;
    border-top: 2px dotted var(--rule);
  }
  .contact {
    position: absolute;
    right: 24px;
    top: 282px;
    margin: 0;
    text-align: right;
    font-size: 15.5px;
    line-height: 21px;
    font-style: normal;
    color: var(--ink-soft);
  }
</style>
</head>
<body>
<main class="canvas">
  <section class="card card-front" aria-label="Card front">
    <div class="dandelion-cluster" role="img" aria-label="Illustration of four white dandelion clocks on tall stems rising from jagged leaves"></div>
    <div class="drifting-seeds" role="img" aria-label="Illustration of white dandelion seeds drifting away in the wind"></div>
    <div class="name-band">
      <p class="name">Maribel Stroud</p>
      <p class="role">NATUROPATH</p>
    </div>
  </section>

  <section class="card card-back" aria-label="Card back">
    <h1 class="back-name">Maribel Stroud</h1>
    <p class="credentials">BHSc Nat, Dip RM</p>
    <p class="modalities">Naturopath, Herbalist, Nutritionist, Iridologist,<br>Remedial Massage Therapist, Reiki Practitioner</p>
    <div class="divider"></div>
    <address class="contact">
      0413 927 186<br>
      Willowfern Haven - (02) 9731 4068<br>
      maribel.stroud@kestrelmail.example<br>
      NHPA 81347
    </address>
  </section>
</main>
</body>
</html>
```